Book cover for publishing doctoral research about various national styles of piano playing.

I need a book cover for a publication of a doctoral research with regard to styles of piano performance characteristic to various nations.

Any images or graphics are optional, typography seems most important, but please feel free to be creative.

I attach the barcode, qsr and publisher's logo in the next few days. (Logo is still being designed).

For various reasons the size of the book is not completely decided yet. Please create your design in 7" x 10", but if at all possible, I would like to ask for files of two sizes, also including 8.5" x 11" in the final submission.

I am looking for a design that looks professional, probably simple, but I am open to any suggestions.

Dear Designers,I would like to thank you all for participation and submitting so many high-quality designs.My final decision was based on the feedback I received from my professional colleagues and potential readers.I would like to wish you all the best for the future.Best wishes,Tadeusz Added Monday, December 21, 2015

Pianists, students, music professionals

Publishing

• Title: Unfolding Seven Harbour Lullabies
• Subtitle: Memories and departures
• Author: Tadeusz Jarocki
• Space for my logo on the front page and the spine.
• On the back page, please include some space for a short biography, 'barcode' and 'qsr' code.
• Please include whatever else you consider necessary.
• Would it be possible to use the same cover to a e-book edition?

```html
<!DOCTYPE html>
<html lang="en">
<head>
<meta charset="utf-8">
<title>Unfolding Seven Harbour Lullabies — Cover</title>
<link href="https://fonts.googleapis.com/css2?family=Oswald:wght@600;700&family=Cormorant+Garamond:wght@500&display=swap" rel="stylesheet">
<style>
  :root {
    --page-bg: #f2f2f2;
    --cover-light: #ffffff;
    --cover-mid: #e6e6e6;
    --cover-low: #bdbdbd;
    --ink: #2c2b2b;
    --band: #3a3838;
    --band-text: #f4f4f4;
  }
  * { margin: 0; padding: 0; box-sizing: border-box; }
  html, body {
    width: 982px; height: 1200px; overflow: hidden;
    background: var(--page-bg);
  }
  .cover {
    position: absolute; left: 71px; top: 0;
    width: 840px; height: 1200px; overflow: hidden;
    background: radial-gradient(ellipse at 50% 40%, var(--cover-light) 0%, #f7f7f7 45%, var(--cover-mid) 100%);
  }
  .keys-art {
    position: absolute; left: 140px; top: 0;
    width: 640px; height: 220px;
    background: linear-gradient(180deg, #4a4a4a 0%, #8a8a8a 55%, rgba(240,240,240,0) 100%);
    opacity: .55;
  }
  .publisher {
    position: absolute; left: 28px; top: 26px;
    display: flex; align-items: center; gap: 8px;
    font-family: "Oswald", sans-serif; font-weight: 600;
    font-size: 15px; letter-spacing: 1px; color: var(--ink);
    text-transform: uppercase;
  }
  .publisher .mark {
    width: 40px; height: 40px; background: var(--ink);
  }
  .title {
    position: absolute; left: 0; top: 268px; width: 100%;
    text-align: center;
    font-family: "Oswald", sans-serif; font-weight: 700;
    font-size: 124px; line-height: 128px;
    letter-spacing: -1px; text-transform: uppercase;
    color: var(--ink);
  }
  .title span { display: block; }
  .lower-shade {
    position: absolute; left: 0; top: 844px; width: 100%; height: 356px;
    background: linear-gradient(180deg, #d8d8d8 0%, #cfcfcf 40%, var(--cover-low) 100%);
  }
  .subtitle-band {
    position: absolute; left: 0; top: 800px; width: 100%; height: 44px;
    background: var(--band);
  }
  .subtitle {
    position: absolute; left: 0; top: 800px; width: 100%; height: 44px;
    text-align: center;
    font-family: "Cormorant Garamond", serif; font-weight: 500;
    font-size: 32px; line-height: 44px; letter-spacing: .5px; text-transform: uppercase;
    color: var(--band-text);
  }
  .author {
    position: absolute; left: 0; top: 888px; width: 100%;
    text-align: center;
    font-family: "Oswald", sans-serif; font-weight: 700;
    font-size: 44px; line-height: 60px; letter-spacing: 3px; text-transform: uppercase;
    color: var(--ink);
  }
</style>
</head>
<body>
  <main class="cover">
    <div class="keys-art" role="img" aria-label="Fading piano keyboard keys descending from the top edge"></div>
    <div class="publisher"><span class="mark"></span><span>Larkhaven Books</span></div>
    <h1 class="title">
      <span>Unfolding</span>
      <span>Seven</span>
      <span>Harbour</span>
      <span>Lullabies</span>
    </h1>
    <div class="lower-shade"></div>
    <div class="subtitle-band"></div>
    <p class="subtitle">Memories and departures</p>
    <p class="author">Tadeusz Jarocki</p>
  </main>
</body>
</html>
```